Harvest Cellar

We need desigin for our main page(concept will be used for other pages also).
We already have a logo, and moqup of our main page(see attch).
You could change layers and positions on moqup, but please use logo, and its colors in design creating. (We have logo in different colors, i attached 2 samples, so you could use also another colors if you wish).

Our bussinees will be something similar to BloomLaunch or Seedwell.io, but with some special features. So main idea: start-ups, donations, investemnets

Designs were prefer:
http://seedwell.io/
http://www.bloomlaunch-example.com/

Brief was updated.

Target Market(s)

Clients are middle aged persons, who interested in new start-ups, investments and so on.

Requirements
Must have
• Design must be neat

```html
<!DOCTYPE html>
<html lang="en">
<head>
<meta charset="utf-8">
<title>Harvest Cellar — Home</title>
<link href="https://fonts.googleapis.com/css2?family=PT+Sans:wght@400;700&family=Arimo:wght@400;700&display=swap" rel="stylesheet">
<style>
:root{
  --red:#e4222a;
  --red-dark:#b8151c;
  --field:#7d0a0f;
  --ink:#222;
  --grey-light:#ddd;
  --footer:#2b2b2b;
  --footer-bottom:#1f1f1f;
  --footer-text:#8a8a8a;
  --white:#fff;
  --green:#7db43c;
  --navy:#1d3347;
}
*{box-sizing:border-box;margin:0;padding:0}
html,body{width:1095px;height:1200px;overflow:hidden}
body{position:relative;background:var(--white);font-family:"PT Sans",sans-serif;color:var(--ink)}
.abs{position:absolute}

/* header */
.brand{left:168px;top:30px;display:flex;align-items:center;gap:8px}
.brand-mark{width:22px;height:22px;border-radius:50%;background:var(--red-dark)}
.brand-name{font-size:21px;font-weight:700;color:var(--navy);white-space:nowrap}
.nav-btn{top:23px;width:120px;height:36px;border-radius:2px;color:var(--white);font-size:11px;display:flex;align-items:center;justify-content:center;box-shadow:0 2px 3px rgba(0,0,0,.35);text-transform:uppercase}
.nav-btn.is-active{background:linear-gradient(#d42a30,#a3141a)}
.nav-btn.is-muted{background:linear-gradient(#6d6d6d,#3f3f3f)}
.search{left:790px;top:16px;width:139px;height:19px;border:1px solid #ccc;font-size:9px;color:#999;padding:3px 6px;display:flex;justify-content:space-between}
.search-icon{width:9px;height:9px;border:1px solid #ccc;border-radius:50%}
.lang{left:797px;top:45px;font-size:9px;color:#888;display:flex;align-items:center;gap:4px}
.lang-box{width:84px;height:18px;border:1px solid #ccc;display:flex;align-items:center;gap:5px;padding:0 5px;color:#888}
.flag{width:14px;height:9px;background:#2a3f8a}

/* hero */
.hero{left:0;top:80px;width:1095px;height:376px;background:linear-gradient(var(--red) 0%,#d41e25 60%,#c0181e 100%)}
.hero-title{top:24px;width:100%;text-align:center;color:var(--white);font-size:24px;font-weight:400}
.hero-copy{top:62px;left:165px;width:765px;text-align:center;color:var(--white);font-size:10.5px;line-height:16px}
.hero-rule{top:106px;left:165px;width:765px;height:1px;background:rgba(255,255,255,.25)}
.stats{top:149px;left:165px;width:196px;list-style:none}
.stats li{height:27.4px;line-height:24px;text-align:right;padding-right:52px;color:var(--white);font-size:8.5px;text-transform:uppercase}
.stats li.is-current{background:rgba(255,255,255,.25);padding-right:36px}
.stats li.is-current::after{content:"‹";font-size:12px;margin-left:12px}
.laptop{left:361px;top:130px;width:361px;height:240px;border-radius:8px;background:#111;border:2px solid #555;padding:12px 10px}
.video{width:100%;height:198px;background:linear-gradient(#0b1a3a,#1b6a9a 55%,#0c1a30)}
.video-bar{height:14px;background:#1a1a1a;margin-top:2px}
.play{left:174px;top:110px;width:46px;height:46px;border-radius:50%;background:rgba(80,80,80,.7);border:1px solid #999}
.play::after{content:"";position:absolute;left:18px;top:13px;border-left:14px solid #ddd;border-top:9px solid transparent;border-bottom:9px solid transparent}
.laptop-base{left:320px;top:370px;width:442px;height:14px;border-radius:0 0 14px 14px;background:linear-gradient(#eee,#aaa)}
.tab{top:126px;height:32px;color:var(--white);font-size:11px;display:flex;align-items:center;justify-content:center}
.tab.is-active{left:746px;width:81px;background:var(--red-dark)}
.tab.is-idle{left:827px;width:103px}
.login{left:722px;top:158px;width:208px;height:146px;background:var(--red-dark);padding:20px 24px;color:var(--white);font-size:7px;text-transform:uppercase}
.field{height:17px;background:var(--field);margin:6px 0 16px}
.login-row{display:flex;justify-content:space-between;align-items:flex-start}
.submit{width:62px;height:17px;background:linear-gradient(#888,#555);font-size:8px;display:flex;align-items:center;justify-content:center;margin-top:-2px}
.check{display:inline-block;width:9px;height:9px;background:#eee;margin-right:6px;vertical-align:middle}
.pager{top:347px;color:rgba(255,255,255,.7);font-size:20px}

/* projects */
.card{top:510px;width:182px;height:380px;border:1px solid var(--grey-light);background:var(--white);text-align:center}
.card-head{height:44px;background:linear-gradient(#d72028,#a5131a);color:var(--white);font-size:14px;line-height:44px;text-transform:uppercase;margin:-1px -1px 0}
.card-title{font-size:18px;font-weight:400;margin:10px 0 8px;color:#333}
.card-img{width:158px;height:82px;margin:0 auto;border:2px solid #ccc}
.card-desc{font-family:Arimo,sans-serif;font-size:8.5px;color:#555;text-align:left;line-height:14px;padding:10px 15px 0}
.badge{display:inline-block;margin-top:4px;width:76px;height:13px;border:1px solid #999;border-radius:5px;background:linear-gradient(#fff,#ddd);font-family:Arimo,sans-serif;font-size:7.5px;color:#777;line-height:11px}
.bar{width:148px;height:11px;border-radius:5px;background:#3c3c3c;margin:4px auto 0;overflow:hidden}
.bar-fill{width:68%;height:100%;background:linear-gradient(#9ccf5a,var(--green))}
.invested{width:150px;height:24px;margin:11px auto 0;border:1px solid var(--grey-light);font-size:9px;color:#555;line-height:22px}
.card-stats{display:flex;justify-content:space-between;width:150px;margin:9px auto 0}
.card-stats span{width:71px;height:19px;background:#666;color:var(--white);font-size:8px;line-height:19px}
.invest-btn{width:148px;height:41px;margin:14px auto 0;background:linear-gradient(#444,#0c0c0c);color:var(--white);font-size:16px;line-height:41px;text-transform:uppercase}

.view-all{left:430px;top:918px;width:219px;height:106px;border-radius:10px;border:1px solid #ccc;background:linear-gradient(#fff,#e6e6e6);box-shadow:0 4px 6px rgba(0,0,0,.25);text-align:center}
.view-all-title{font-size:22px;color:#888;margin-top:10px}
.view-all-sub{font-family:Arimo,sans-serif;font-size:10px;font-weight:700;color:#333;margin-top:4px}
.view-all-btn{width:111px;height:23px;margin:8px auto 0;background:linear-gradient(#d72028,#a5131a);color:var(--white);font-family:Arimo,sans-serif;font-weight:700;font-size:10px;line-height:23px}

/* footer */
.footer{left:0;top:1053px;width:1095px;height:109px;background:var(--footer)}
.footer-col{top:22px;width:360px}
.footer-col h3{font-weight:400;font-size:14px;color:#eee;text-transform:uppercase;margin-bottom:9px}
.footer-col p{font-size:8px;color:var(--footer-text);line-height:14px}
.footer-rule{left:548px;top:24px;width:1px;height:64px;background:#444}
.footer-bottom{left:0;top:1162px;width:1095px;height:38px;background:var(--footer-bottom)}
.copyright{left:167px;top:14px;font-size:7.5px;color:#666;text-transform:uppercase}
.social{top:14px;width:10px;height:10px;border-radius:50%;background:#666}
</style>
</head>
<body>

<header>
  <div class="abs brand">
    <span class="brand-mark"></span>
    <span class="brand-name">Harvest Cellar</span>
  </div>
  <nav>
    <div class="abs nav-btn is-active" style="left:366px">How it works</div>
    <div class="abs nav-btn is-muted" style="left:499px">Project review</div>
    <div class="abs nav-btn is-muted" style="left:632px">Virtual office</div>
  </nav>
  <div class="abs search"><span>Search</span><span class="search-icon"></span></div>
  <div class="abs lang">Language :
    <div class="lang-box"><span class="flag"></span>English <span style="margin-left:auto">⌄</span></div>
  </div>
</header>

<section class="abs hero">
  <h1 class="abs hero-title">WELCOME TO HARVEST CELLAR</h1>
  <p class="abs hero-copy">Lorem Ipsum is simply dummy text of the printing and typesetting industry. Lorem Ipsum has been the industry's standard dummy text ever since the 1500s, when an unknown printer took a galley of type and scrambled it to make a type specimen book.</p>
  <div class="abs hero-rule"></div>
  <ul class="abs stats">
    <li class="is-current">$ 50 000 000 of investments</li>
    <li>1600 start-ups</li>
    <li>700 organizations</li>
    <li>10 000 investors</li>
    <li>5000 employes</li>
    <li>2000 partners</li>
    <li>$10 000 000 pf profuit</li>
  </ul>
  <div class="abs laptop">
    <div class="video" role="img" aria-label="Video still: rows of computer monitors under streams of binary digits"></div>
    <div class="video-bar"></div>
    <div class="abs play"></div>
  </div>
  <div class="abs laptop-base"></div>
  <div class="abs tab is-active">LOGIN</div>
  <div class="abs tab is-idle">REGISTRATION</div>
  <form class="abs login">
    <div>Email or phone number</div>
    <div class="field"></div>
    <div>Password</div>
    <div class="field"></div>
    <div class="login-row">
      <div>Forget your password<br><br><span class="check"></span>Safe login</div>
      <div class="submit">SUBMIT</div>
    </div>
  </form>
  <div class="abs pager" style="left:893px">‹</div>
  <div class="abs pager" style="left:916px">›</div>
</section>

<main>
  <article class="abs card" style="left:165px">
    <div class="card-head">Recommended</div>
    <h2 class="card-title">PROJECT-A</h2>
    <div class="card-img" role="img" aria-label="Blue tunnel of binary code" style="background:linear-gradient(135deg,#1a2a8a,#6a7ae0,#101a5a)"></div>
    <p class="card-desc">Very intersting thing short description of the project</p>
    <span class="badge">68 % Success</span>
    <div class="bar"><div class="bar-fill"></div></div>
    <div class="invested">$90 000 invested</div>
    <div class="card-stats"><span>200 investors</span><span>23 days left</span></div>
    <div class="invest-btn">Invest</div>
  </article>
  <article class="abs card" style="left:358px">
    <div class="card-head">Popular</div>
    <h2 class="card-title">PROJECT-B</h2>
    <div class="card-img" role="img" aria-label="Padlock and chain on a laptop keyboard" style="background:linear-gradient(135deg,#c8ccd4,#3a3a3a,#9aa0a8)"></div>
    <p class="card-desc">Very intersting thing short description of the project</p>
    <span class="badge">68 % Success</span>
    <div class="bar"><div class="bar-fill"></div></div>
    <div class="invested">$90 000 invested</div>
    <div class="card-stats"><span>200 investors</span><span>23 days left</span></div>
    <div class="invest-btn">Invest</div>
  </article>
  <article class="abs card" style="left:553px">
    <div class="card-head">Most invested</div>
    <h2 class="card-title">PROJECT-C</h2>
    <div class="card-img" role="img" aria-label="Glowing padlock on a circuit board" style="background:radial-gradient(circle,#8fe0ff,#1a7ad0 45%,#0a2a70)"></div>
    <p class="card-desc">Very intersting thing short description of the project</p>
    <span class="badge">68 % Success</span>
    <div class="bar"><div class="bar-fill"></div></div>
    <div class="invested">$90 000 invested</div>
    <div class="card-stats"><span>200 investors</span><span>23 days left</span></div>
    <div class="invest-btn">Invest</div>
  </article>
  <article class="abs card" style="left:747px">
    <div class="card-head">New</div>
    <h2 class="card-title">PROJECT-D</h2>
    <div class="card-img" role="img" aria-label="Network cable locked with a combination padlock" style="background:linear-gradient(135deg,#d8dde6,#4a6ab0,#b8c0cc)"></div>
    <p class="card-desc">Very intersting thing short description of the project</p>
    <span class="badge">68 % Success</span>
    <div class="bar"><div class="bar-fill"></div></div>
    <div class="invested">$90 000 invested</div>
    <div class="card-stats"><span>200 investors</span><span>23 days left</span></div>
    <div class="invest-btn">Invest</div>
  </article>

  <div class="abs view-all">
    <div class="view-all-title">View all Projects</div>
    <div class="view-all-sub">More then 1000 Projects</div>
    <div class="view-all-btn">Yes</div>
  </div>
</main>

<footer>
  <div class="abs footer">
    <div class="abs footer-col" style="left:164px">
      <h3>Intersting informations</h3>
      <p>Lorem Ipsum is simply dummy text of the printing and typesetting industry. Lorem Ipsum has been the industry's standard dummy text ever since the 1500s, when an unknown printer took a galley of type and scrambled it to make a type specimen book.</p>
    </div>
    <div class="abs footer-rule"></div>
    <div class="abs footer-col" style="left:575px">
      <h3>Investment projects</h3>
      <p>Lorem Ipsum is simply dummy text of the printing and typesetting industry. Lorem Ipsum has been the industry's standard dummy text ever since the 1500s, when an unknown printer took a galley of type and scrambled it to make a type specimen book.</p>
    </div>
  </div>
  <div class="abs footer-bottom">
    <div class="abs copyright">© 2013 Harvest Cellar. All rights reserved.</div>
    <span class="abs social" style="left:762px"></span>
    <span class="abs social" style="left:793px"></span>
    <span class="abs social" style="left:825px"></span>
    <span class="abs social" style="left:855px"></span>
    <span class="abs social" style="left:886px"></span>
    <span class="abs social" style="left:917px"></span>
  </div>
</footer>

</body>
</html>
```